velto renovation roof

We need a flyer for a new york based company called velto renovations. We are looking to promote our roofing/window/siding/concrete service.

We are a construction company with over 30 years in the business, but have set up a new company to specialize in roofing - windows - siding. We do offer general renovation service both interior (tiles, paint , Plakwall, etc) as well as concrete work (driveways, sidewalk) but we think it may be to much information for the flyer. We are fully insured and licensed

We are open to all ideas (I will include a picture of a design that caught our eye from your site).

Target Market(s)

home owners, building managers in the tri state area. We are a New York based company

Industry/Entity Type

Construction

```html
<!DOCTYPE html>
<html lang="en">
<head>
<meta charset="utf-8">
<title>Velto Renovations – Rack Card</title>
<link rel="stylesheet" href="https://fonts.googleapis.com/css2?family=Open+Sans:wght@400;600;700;800&family=Arimo:wght@400;700&display=swap">
<style>
  :root {
    --page: #e4e4e4;
    --sky: #bfe1f5;
    --navy: #24215f;
    --red: #e5222b;
    --white: #ffffff;
    --ink: #111111;
    --teal: #1f6f73;
  }
  * { box-sizing: border-box; margin: 0; padding: 0; }
  html, body { width: 1200px; height: 970px; overflow: hidden; }
  body {
    background: var(--page);
    display: flex; align-items: center; justify-content: center;
    font-family: "Open Sans", Arial, sans-serif;
  }
  .rack-card {
    width: 1040px; height: 440px;
    display: flex; flex-direction: column;
    background: var(--white);
    box-shadow: 0 6px 18px rgba(0,0,0,.18);
  }
  .service-strip {
    height: 52px; flex: none; background: var(--sky);
    display: flex; align-items: center; padding-left: 22px;
    font-weight: 800; font-size: 20px; color: var(--ink); letter-spacing: .5px;
  }
  .service-strip .sep { margin: 0 9px; font-weight: 400; }
  .message-band {
    height: 200px; flex: none; background: var(--navy); color: var(--white);
    display: flex; justify-content: space-between; align-items: center;
    padding: 0 36px 0 40px;
  }
  .pitch { font-size: 23px; line-height: 1.3; }
  .pitch strong { font-weight: 700; }
  .pitch .call-out {
    display: block; color: var(--red);
    font-family: "Arimo", Arial, sans-serif; font-size: 34px; line-height: 1.15; margin-top: 4px;
  }
  .brand { display: flex; flex-direction: column; align-items: flex-end; gap: 14px; }
  .licence-badge { position: relative; width: 150px; height: 78px; }
  .licence-badge .ribbon {
    position: absolute; left: 0; right: 0; top: 40px; height: 22px; background: var(--red);
  }
  .licence-badge .seal {
    position: absolute; left: 25px; top: 0; width: 100px; height: 78px;
    background: var(--teal); border: 3px solid var(--white); border-radius: 10px;
    display: flex; align-items: center; justify-content: center; text-align: center;
    font-size: 13px; font-weight: 800; line-height: 1.2; letter-spacing: .5px; color: var(--white);
  }
  .brand-name {
    display: flex; align-items: center; gap: 10px;
    font-size: 38px; font-weight: 700; letter-spacing: 1px; line-height: 1;
  }
  .brand-name .mark { width: 22px; height: 22px; background: var(--white); }
  .photo-row { height: 120px; flex: none; display: flex; }
  .photo { flex: 1; }
  .photo.concrete { background: linear-gradient(135deg, #a9a59c, #c9c5bb 60%, #7d6a58); }
  .photo.roofer { background: linear-gradient(180deg, #9fc6e6, #b48a6a 55%, #7a5a44); }
  .photo.window-install { background: linear-gradient(160deg, #e9ecec, #c7d0cf 50%, #3b4a6a); }
  .photo.window-room { background: linear-gradient(180deg, #f2f2ee, #d7d4cb 60%, #8b8070); }
  .contact-band {
    flex: 1; background: var(--red); color: var(--white);
    display: flex; align-items: center; justify-content: space-between;
    padding: 0 40px; font-family: "Arimo", Arial, sans-serif;
  }
  .contact-band .cta { font-size: 30px; }
  .contact-item { display: flex; align-items: center; gap: 10px; font-size: 24px; font-weight: 700; }
</style>
</head>
<body>
  <article class="rack-card">
    <div class="service-strip">
      ROOFING<span class="sep">|</span>WINDOWS<span class="sep">|</span>SIDING<span class="sep">|</span>GENERAL RENOVATION<span class="sep">|</span>CONCRETE SERVICE etc
    </div>

    <section class="message-band">
      <p class="pitch">
        Do you require<br>
        <strong>WINDOW REPLACING, ROOFING EMERGENCY?</strong><br>
        <strong>Or GENERAL RENOVATION?</strong><br>
        Get complete service. Call us and let us know....
        <span class="call-out">WHAT YOU WANT!</span>
      </p>
      <div class="brand">
        <div class="licence-badge">
          <span class="ribbon"></span>
          <span class="seal">LICENSED &amp;<br>INSURED</span>
        </div>
        <div class="brand-name"><span class="mark"></span>VELTORENO</div>
      </div>
    </section>

    <div class="photo-row">
      <div class="photo concrete" role="img" aria-label="Worker smoothing fresh concrete with a trowel"></div>
      <div class="photo roofer" role="img" aria-label="Roofer nailing shingles on a roof"></div>
      <div class="photo window-install" role="img" aria-label="Installer fitting a new window frame"></div>
      <div class="photo window-room" role="img" aria-label="Bright room with newly replaced windows"></div>
    </div>

    <footer class="contact-band">
      <span class="cta">Contact Us Today</span>
      <span class="contact-item">
        <svg width="24" height="24" viewBox="0 0 24 24" aria-hidden="true">
          <circle cx="12" cy="12" r="10" fill="none" stroke="#fff" stroke-width="2"/>
          <ellipse cx="12" cy="12" rx="4.5" ry="10" fill="none" stroke="#fff" stroke-width="1.6"/>
          <line x1="2" y1="12" x2="22" y2="12" stroke="#fff" stroke-width="1.6"/>
        </svg>
        www.VELTORENO.net
      </span>
      <span class="contact-item">
        <svg width="24" height="24" viewBox="0 0 24 24" aria-hidden="true">
          <circle cx="12" cy="12" r="10" fill="none" stroke="#fff" stroke-width="2"/>
          <path d="M8.5 7c.8-.6 1.6.2 2 1l.6 1.3c.2.6-.3 1-.7 1.4.6 1.3 1.5 2.2 2.8 2.8.4-.4.8-.9 1.4-.7l1.3.6c.8.4 1.6 1.2 1 2-.8 1-2 1.4-3.3.9-2.6-1-4.7-3.1-5.7-5.7-.5-1.3-.1-2.5.6-3.3z" fill="#fff"/>
        </svg>
        347-555-0148
      </span>
    </footer>
  </article>
</body>
</html>
```